VOLT Outreach Sell Sheets Design

I need a flyer that I can use to market and advertise my business utilizing the logo that you already created. I will attach in detail a copy of the design specifics for the layout of the flyer as well as the content of each flyer. The color scheme will be the same as the logo you designed. Blues, greys, blacks, White

Target Market(s)

Insurance

Industry/Entity Type

Insurance Blue

Font styles to use
Sans Serif

Colors
3176b5
cfdeed
eaf1f7

Requirements
Must have
• I need 6 individual sheets on 8.5 X 11. The layout will be as per the layout I have marked up and described in the brief. The only change on each flyer is the content which I have submitted 6 descriptions along with content. The logo and color scheme will be as described In the brief.
Nice to have
• No preference
Should not have
• No preference

```html
<!DOCTYPE html>
<html lang="en">
<head>
<meta charset="utf-8">
<title>VOLT Outreach – Audit Sell Sheet</title>
<link rel="stylesheet" href="https://fonts.googleapis.com/css2?family=Arimo:wght@400;700&family=Raleway:wght@800&family=Cinzel:wght@600&display=swap">
<style>
  :root {
    --brand-blue: #2f76b5;
    --brand-mid: #cfdeed;
    --brand-pale: #eaf1f7;
    --accent-cyan: #1ea3e0;
    --ink: #1f2a3a;
    --white: #ffffff;
    --paper: #ffffff;
  }
  * { margin: 0; padding: 0; box-sizing: border-box; }
  html, body { width: 960px; height: 1200px; overflow: hidden; background: var(--paper); }
  .sheet { position: relative; width: 960px; height: 1200px; font-family: "Arimo", Arial, sans-serif; }

  .slug { position: absolute; left: 72px; top: 22px; font-size: 9px; color: var(--ink); }
  .printer-marks { position: absolute; inset: 0; pointer-events: none; }

  .band { position: absolute; left: 65px; width: 828px; background: var(--brand-blue); }
  .band--top { top: 65px; height: 55px; }
  .band--bottom { top: 1080px; height: 53px; }
  .band--tagline { top: 802px; height: 48px; display: flex; align-items: center; padding-left: 47px; }
  .tagline { color: var(--white); font-weight: 700; font-size: 25px; letter-spacing: 0.2px; }

  .hero-photo {
    position: absolute; left: 408px; top: 120px; width: 485px; height: 682px;
    background: linear-gradient(160deg, #dfe6ee 0%, #a9b8c9 28%, #c7d6e6 52%, #e9eef4 72%, #5e7187 100%);
  }
  .values { position: absolute; left: 454px; top: 120px; list-style: none; }
  .values li {
    position: absolute; left: 0; white-space: nowrap;
    font-family: "Raleway", "Arial Black", sans-serif; font-weight: 800; font-size: 58px;
    color: var(--white); letter-spacing: -1px; text-shadow: 0 2px 6px rgba(40,50,70,0.35);
  }

  .brand { position: absolute; left: 111px; top: 166px; display: flex; align-items: center; gap: 10px; }
  .brand__square { width: 44px; height: 44px; background: var(--brand-blue); }
  .brand__name { font-size: 27px; font-weight: 700; color: var(--brand-blue); }
  .service-name {
    position: absolute; left: 160px; width: 156px; top: 243px; text-align: center;
    font-family: "Cinzel", Georgia, serif; font-weight: 600; font-size: 21px; letter-spacing: 3px; color: var(--accent-cyan);
  }
  .promise { position: absolute; left: 172px; top: 370px; list-style: none; }
  .promise li { font-weight: 700; font-size: 31px; line-height: 48px; color: var(--brand-blue); }

  .detail-panel { position: absolute; left: 65px; top: 850px; width: 828px; height: 230px; background: var(--brand-mid); }
  .detail-photo {
    position: absolute; left: 408px; top: 850px; width: 485px; height: 230px;
    background: linear-gradient(180deg, #c3d2e2 0%, #e6edf4 55%, #d6e1ec 100%);
  }
  .report-photo {
    position: absolute; left: 110px; top: 878px; width: 257px; height: 173px;
    background: linear-gradient(135deg, #cfe6ef 0%, #ffffff 40%, #f3f5f7 75%, #6f7782 100%);
  }
</style>
</head>
<body>
<main class="sheet">
  <div class="slug">AUDIT (front)</div>

  <svg class="printer-marks" width="960" height="1200" viewBox="0 0 960 1200" aria-hidden="true">
    <g class="color-bar">
      <rect x="296" y="24" width="23" height="23" fill="#fff9c4"/><rect x="319" y="24" width="23" height="23" fill="#fff48a"/>
      <rect x="342" y="24" width="23" height="23" fill="#ffef4d"/><rect x="365" y="24" width="23" height="23" fill="#ffec00"/>
      <rect x="388" y="24" width="23" height="23" fill="#b3e4f7"/><rect x="411" y="24" width="23" height="23" fill="#7cd2f3"/>
      <rect x="434" y="24" width="23" height="23" fill="#2fbaeb"/><rect x="457" y="24" width="23" height="23" fill="#00a5e6"/>
      <rect x="480" y="24" width="23" height="23" fill="#f8c9dc"/><rect x="503" y="24" width="23" height="23" fill="#f49cc0"/>
      <rect x="526" y="24" width="23" height="23" fill="#ef5fa0"/><rect x="549" y="24" width="23" height="23" fill="#e6007e"/>
      <rect x="572" y="24" width="23" height="23" fill="#c6c6c6"/><rect x="595" y="24" width="23" height="23" fill="#939393"/>
      <rect x="618" y="24" width="23" height="23" fill="#575757"/><rect x="641" y="24" width="23" height="23" fill="#000"/>
    </g>
    <use href="#bar" />
    <g transform="translate(0 1126)">
      <rect x="296" y="24" width="23" height="23" fill="#fff9c4"/><rect x="319" y="24" width="23" height="23" fill="#fff48a"/>
      <rect x="342" y="24" width="23" height="23" fill="#ffef4d"/><rect x="365" y="24" width="23" height="23" fill="#ffec00"/>
      <rect x="388" y="24" width="23" height="23" fill="#b3e4f7"/><rect x="411" y="24" width="23" height="23" fill="#7cd2f3"/>
      <rect x="434" y="24" width="23" height="23" fill="#2fbaeb"/><rect x="457" y="24" width="23" height="23" fill="#00a5e6"/>
      <rect x="480" y="24" width="23" height="23" fill="#f8c9dc"/><rect x="503" y="24" width="23" height="23" fill="#f49cc0"/>
      <rect x="526" y="24" width="23" height="23" fill="#ef5fa0"/><rect x="549" y="24" width="23" height="23" fill="#e6007e"/>
      <rect x="572" y="24" width="23" height="23" fill="#c6c6c6"/><rect x="595" y="24" width="23" height="23" fill="#939393"/>
      <rect x="618" y="24" width="23" height="23" fill="#575757"/><rect x="641" y="24" width="23" height="23" fill="#000"/>
    </g>
    <g class="registration" fill="none" stroke="#000" stroke-width="1">
      <circle cx="270" cy="36" r="8"/><path d="M258 36h24M270 24v24"/>
      <circle cx="692" cy="36" r="8"/><path d="M680 36h24M692 24v24"/>
      <circle cx="270" cy="1163" r="8"/><path d="M258 1163h24M270 1151v24"/>
      <circle cx="692" cy="1163" r="8"/><path d="M680 1163h24M692 1151v24"/>
    </g>
    <g class="crop-marks" stroke="#000" stroke-width="1">
      <path d="M48 72h17M72 48v17"/>
      <path d="M893 72h19M888 48v17"/>
      <path d="M48 1128h17M72 1133v17"/>
      <path d="M893 1128h19M888 1133v17"/>
    </g>
  </svg>

  <div class="band band--top"></div>

  <div class="hero-photo" role="img" aria-label="Close-up photo of a hand pointing a silver pen at pie charts on a printed report"></div>
  <ul class="values">
    <li style="top:133px">PROFESSIONAL</li>
    <li style="top:248px">RELIABLE</li>
    <li style="top:363px">TRUST</li>
    <li style="top:479px">QUALITY</li>
  </ul>

  <div class="brand">
    <span class="brand__square"></span>
    <span class="brand__name">VOLT Outreach</span>
  </div>
  <div class="service-name">AUDIT</div>

  <ul class="promise">
    <li>Fast,</li>
    <li>Friendly,</li>
    <li>Honest</li>
  </ul>

  <div class="band band--tagline"><span class="tagline">LEADERS IN CLAIMS MANAGEMENT</span></div>

  <div class="detail-panel"></div>
  <div class="detail-photo" role="img" aria-label="Faded photo of a printed data table listing countries"></div>
  <div class="report-photo" role="img" aria-label="Photo of an audit report checklist with a fountain pen"></div>

  <div class="band band--bottom"></div>
</main>
</body>
</html>
```